Financial advisory firm needs new business card design

Business card design , simple , elegant, professional. Will use existing logo. One side should be a solid blue background (matching blue in Logo) . info side should have basic info, maybe two color panes. one white, one a different color..maybe light grey. Please visit our website to get feel for colors and business. www.tallowmeadwealth.com

Industry/Entity Type

Financial Service

Contact Information for Business Card

Basic info..minimalist, modern, approach

Colors

Designer to choose colors to be used in the design.

Requirements
Must have
• Important regulatory requirement. The following disclosure MUST be included somewhere on the business card. It can be either front, or back, and it may be in a smaller font (but has to be legible). My interest is to satisfy the requirement with the least possible disruption to the beauty of the card design.
• All securities offered through the Harrowgate Capital, Inc. Oakhurst Lane, NJ. Member QOLTA/DWEM. Advisory services provided through HC Advisory Services, Inc. an PBR Registered Investment Advisor.

```html
<!DOCTYPE html>
<html lang="en">
<head>
<meta charset="utf-8">
<title>Tallowmead Wealth – Business Card</title>
<link href="https://fonts.googleapis.com/css2?family=Jost:wght@400;500&family=Montserrat:wght@700&display=swap" rel="stylesheet">
<style>
  :root {
    --stage: #222324;
    --brand-blue: #0a4c84;
    --brand-blue-deep: #083d6b;
    --icon-blue: #1f7fc9;
    --paper: #ffffff;
    --ink: #1d1d1d;
    --muted: #5a5a5a;
    --rule: #1a1a1a;
  }
  * { margin: 0; padding: 0; box-sizing: border-box; }
  html, body {
    width: 1200px; height: 900px; overflow: hidden;
    background: var(--stage);
    font-family: "Jost", sans-serif;
  }
  .card {
    position: absolute;
    left: 285px;
    width: 630px; height: 360px;
    overflow: hidden;
  }
  .card-back { top: 70px; background: var(--brand-blue); }
  .card-back .brand-mark {
    position: absolute; right: 56px; bottom: 48px;
    font-family: "Jost", sans-serif; font-weight: 500;
    font-size: 15px; letter-spacing: 1.5px;
    color: var(--brand-blue-deep);
    text-transform: uppercase;
  }
  .card-front { top: 470px; background: var(--paper); }
  .front-band {
    position: absolute; left: 0; top: 0;
    width: 100%; height: 132px;
    background: var(--brand-blue);
  }
  .front-rule {
    position: absolute; left: 0; top: 137px;
    width: 100%; height: 2px;
    background: var(--rule);
  }
  .brand-logo {
    position: absolute; left: 280px; top: 54px;
    display: flex; align-items: center; gap: 10px;
    color: var(--paper);
    font-family: "Jost", sans-serif; font-weight: 500;
    font-size: 24px; letter-spacing: 1px;
    text-transform: uppercase;
    white-space: nowrap;
  }
  .brand-logo .dot {
    width: 13px; height: 13px; border-radius: 50%;
    background: var(--paper);
  }
  .contact {
    position: absolute; left: 290px; top: 152px;
    color: var(--ink);
  }
  .person-name {
    font-family: "Montserrat", sans-serif; font-weight: 700;
    font-size: 18px; letter-spacing: 1px;
    color: var(--brand-blue);
    text-transform: uppercase;
    line-height: 22px;
  }
  .person-role { font-size: 15px; line-height: 18px; margin-bottom: 8px; }
  .contact-list { list-style: none; }
  .contact-list li {
    display: flex; align-items: center; gap: 10px;
    font-size: 16px; line-height: 22px;
  }
  .contact-list svg { width: 15px; height: 15px; flex: none; }
  .address { font-size: 16px; line-height: 20px; margin-top: 8px; }
  .disclosure {
    position: absolute; left: 24px; right: 24px; bottom: 8px;
    font-size: 9px; line-height: 11px;
    color: var(--muted);
    text-align: center;
  }
</style>
</head>
<body>
  <section class="card card-back" aria-label="Card back">
    <span class="brand-mark">Tallowmead Wealth</span>
  </section>

  <section class="card card-front" aria-label="Card front">
    <div class="front-band"></div>
    <div class="front-rule"></div>
    <div class="brand-logo"><span class="dot"></span>Tallowmead Wealth</div>

    <div class="contact">
      <p class="person-name">Devlin Marsh</p>
      <p class="person-role">Sales Manager</p>
      <ul class="contact-list">
        <li>
          <svg viewBox="0 0 16 16" aria-hidden="true"><circle cx="8" cy="8" r="7" fill="none" stroke="var(--icon-blue)" stroke-width="1.3"/><path d="M5.5 4.5l1.5 1.5-1 1c.6 1.2 1.4 2 2.6 2.6l1-1 1.5 1.5-1.2 1.2C7.6 11 5 8.4 4.3 5.7z" fill="var(--icon-blue)"/></svg>
          (555) 214-0386
        </li>
        <li>
          <svg viewBox="0 0 16 16" aria-hidden="true"><rect x="1.5" y="3.5" width="13" height="9" fill="none" stroke="var(--icon-blue)" stroke-width="1.3"/><path d="M1.5 3.5L8 9l6.5-5.5" fill="none" stroke="var(--icon-blue)" stroke-width="1.3"/></svg>
          info@tallowmeadwealth.com
        </li>
        <li>
          <svg viewBox="0 0 16 16" aria-hidden="true"><circle cx="8" cy="8" r="7" fill="none" stroke="var(--icon-blue)" stroke-width="1.3"/><ellipse cx="8" cy="8" rx="3" ry="7" fill="none" stroke="var(--icon-blue)" stroke-width="1.1"/><path d="M1 8h14M2.5 4.5h11M2.5 11.5h11" stroke="var(--icon-blue)" stroke-width="1.1"/></svg>
          www.tallowmeadwealth.com
        </li>
      </ul>
      <p class="address">48 Quarry Bend Road, Suite 110<br>Fenwick, NJ 07000</p>
    </div>

    <p class="disclosure">All securities offered through Harrowgate Capital, Inc. Oakhurst Lane, NJ. Member QOLTA/DWEM.<br>Advisory services provided through HC Advisory Services, Inc. a PBR Registered Investment Advisor.</p>
  </section>
</body>
</html>
```